Business Card Re-Design/Update

We'd like to update out business cards. I've included our current "Style guide" which has the colour scheme of the organisation in it. I've also included the branding files with logos etc in them.

I've also included a copy of one of our existing cards so that you can see how ugly/dated they look. I'd like a fresh modern corporate look.

Target Market(s)

These are for our clients, potential clients, industry contacts - like all business cards

Contact Information for Business Card

Name
Position
Company Address - Level 1, 47 Garnet Lane, Toowong Qld 4066
Direct Phone
mobile
Email
Website -www.korvalnet.com.au
Logo

Colors

Designer to choose colors to be used in the design.

Requirements
Must have
• Main Logo
• Cards will need to be editable to be able to personalize them for each new employee.
Nice to have
• The MapOUT, HandOVER, UpKEEP would be okay to have if they can be sensibly and professionally added to the look without detracting from the main imagery.
• Maybe they could go on the back of the card? will leave this to your creative discretion as to whether/where they fit.
Should not have
• Should not have decorative or script fonts

```html
<!DOCTYPE html>
<html lang="en">
<head>
<meta charset="utf-8">
<title>korvalnet business card</title>
<link rel="stylesheet" href="https://fonts.googleapis.com/css2?family=Inter:wght@400;500;600&display=swap">
<style>
  :root {
    --backdrop: #3a3a3a;
    --card: #ffffff;
    --ink: #1c1c1c;
    --ink-soft: #444444;
    --brand-red: #e3000f;
    --name-red: #e53333;
    --plan-green: #55cc11;
    --deliver-blue: #3399ee;
    --sustain-purple: #bb11ee;
  }
  * { margin: 0; padding: 0; box-sizing: border-box; }
  html, body { width: 1001px; height: 1200px; overflow: hidden; }
  body {
    position: relative;
    background: var(--backdrop);
    font-family: "Inter", Arial, sans-serif;
    color: var(--ink);
  }
  .card {
    position: absolute;
    left: 41px;
    width: 917px;
    height: 550px;
    background: var(--card);
  }
  .card--front { top: 26px; }
  .card--back { top: 627px; }

  .wordmark {
    position: absolute;
    display: flex;
    align-items: center;
    gap: 18px;
    font-weight: 500;
    letter-spacing: -1px;
    color: var(--ink);
    white-space: nowrap;
  }
  .wordmark__mark {
    display: block;
    background: var(--brand-red);
  }
  .card--front .wordmark {
    left: 0; right: 0; top: 232px;
    justify-content: center;
    font-size: 74px;
    line-height: 86px;
  }
  .card--front .wordmark__mark { width: 58px; height: 58px; }
  .card--back .wordmark {
    right: 50px; top: 52px;
    font-size: 66px;
    line-height: 80px;
  }
  .card--back .wordmark__mark { width: 52px; height: 52px; }

  .person { position: absolute; left: 57px; top: 150px; }
  .person__name {
    font-size: 39px;
    font-weight: 600;
    line-height: 44px;
    color: var(--name-red);
  }
  .person__role {
    font-size: 29px;
    font-weight: 400;
    line-height: 34px;
    color: var(--ink);
  }
  .contact {
    position: absolute;
    left: 57px; top: 252px;
    list-style: none;
    font-size: 27px;
    line-height: 28px;
    color: var(--ink-soft);
  }

  .services {
    position: absolute;
    left: 57px; right: 50px; top: 470px;
    display: flex;
    justify-content: space-between;
    list-style: none;
  }
  .service {
    display: flex;
    align-items: center;
    gap: 10px;
    font-size: 40px;
    font-weight: 500;
    line-height: 48px;
    letter-spacing: -0.5px;
  }
  .service__mark { width: 34px; height: 34px; display: block; }
  .service--map { color: var(--plan-green); }
  .service--map .service__mark { background: var(--plan-green); }
  .service--hand { color: var(--deliver-blue); }
  .service--hand .service__mark { background: var(--deliver-blue); }
  .service--keep { color: var(--sustain-purple); }
  .service--keep .service__mark { background: var(--sustain-purple); }
</style>
</head>
<body>
  <section class="card card--front" aria-label="Card front">
    <div class="wordmark"><span class="wordmark__mark"></span>korvalnet</div>
  </section>

  <section class="card card--back" aria-label="Card back">
    <div class="wordmark"><span class="wordmark__mark"></span>korvalnet</div>

    <div class="person">
      <p class="person__name">Maren Holloway</p>
      <p class="person__role">Business Development Manager</p>
    </div>

    <ul class="contact">
      <li>M +61 (0)412 555 019</li>
      <li>D +61 (0)7 3555 0142</li>
      <li>E mholloway@korvalnet.com.au</li>
      <li>Level 1, 47 Garnet Lane, Toowong Qld 4066</li>
      <li>www.korvalnet.com.au</li>
    </ul>

    <ul class="services">
      <li class="service service--map"><span class="service__mark"></span>MapOUT</li>
      <li class="service service--hand"><span class="service__mark"></span>HandOVER</li>
      <li class="service service--keep"><span class="service__mark"></span>UpKEEP</li>
    </ul>
  </section>
</body>
</html>
```